Handout Flyer For Medical Practice (This is Exciting!)

We need a single page handout that showcases the doctors in our medical practice and their specific specialities.

On the front I would like the pictures of the Doctors, names and their specialties. One the back, Map and Contact information for the practice

Attached in the files is what we are currently using and we do want anything that looks such as that.

Industry/Entity Type

Medical

Font styles to use
Serif

Colors
3176b5
0456a4

Requirements
Must have
• Up to date look. Would like a modern touch.

```html
<!DOCTYPE html>
<html lang="en">
<head>
<meta charset="utf-8">
<title>Harlow Ridge Joint &amp; Motion Clinic – Handout</title>
<link rel="stylesheet" href="https://fonts.googleapis.com/css2?family=Arimo:wght@400&family=Open+Sans:wght@400&display=swap">
<style>
  :root{
    --brand-blue:#0456a4;
    --brand-blue-light:#3176b5;
    --brand-navy:#0c4a96;
    --paper:#ffffff;
    --stage:#2e2e2e;
    --ink:#111111;
    --map-tone-a:#ece8df;
    --map-tone-b:#d9d5cc;
    --photo-tone-a:#b9bcc2;
    --photo-tone-b:#6f737b;
    --pin-red:#d8352b;
  }
  *{box-sizing:border-box;margin:0;padding:0}
  html,body{width:1200px;height:1200px;overflow:hidden;background:var(--stage)}
  .sheet{position:absolute;top:184px;width:528px;height:745px;background:var(--paper);overflow:hidden}
  .sheet--front{left:46px}
  .sheet--back{left:621px}

  .front-shapes{position:absolute;inset:0}
  .brand{position:absolute;top:38px;left:0;right:0;display:flex;align-items:center;justify-content:center;gap:10px}
  .brand__dot{width:14px;height:14px;border-radius:50%;background:var(--brand-blue)}
  .brand__name{font-family:"Arimo",sans-serif;font-weight:400;color:var(--brand-blue);font-size:25px;line-height:28px}

  .doctor{position:absolute;width:109px;height:182px;background:var(--paper);padding:4px;text-align:center;font-family:"Arimo",sans-serif}
  .doctor__photo{display:block;width:100%;height:131px;background:linear-gradient(160deg,var(--photo-tone-a),var(--photo-tone-b))}
  .doctor__name{margin-top:9px;font-size:8.2px;color:var(--brand-navy);white-space:nowrap}
  .doctor__role{font-size:4.6px;line-height:5.4px;color:var(--brand-navy);margin-top:2px}

  .about{position:absolute;left:60px;right:60px;top:650px;font-family:"Arimo",sans-serif;font-size:11.4px;line-height:13.6px;color:var(--brand-blue);text-align:center}

  .map{position:absolute;left:0;top:0;width:528px;height:333px;background:linear-gradient(135deg,var(--map-tone-a),var(--map-tone-b))}
  .locate{position:absolute;left:156px;top:391px;display:flex;align-items:flex-end;gap:2px}
  .locate__label{font-family:"Open Sans",sans-serif;font-size:25px;color:var(--ink);margin-bottom:2px}
  .contact{position:absolute;left:0;right:0;top:513px;font-family:"Open Sans",sans-serif;font-size:28px;line-height:42px;color:var(--ink);text-align:center;font-style:normal}
  .contact__phone{display:inline-flex;align-items:center;gap:10px}
  .site-band{position:absolute;left:0;bottom:0;width:100%;height:48px;background:var(--brand-blue);display:flex;align-items:center;justify-content:center;gap:10px;font-family:"Open Sans",sans-serif;font-size:19px;color:#fff}
</style>
</head>
<body>

<section class="sheet sheet--front">
  <svg class="front-shapes" width="528" height="745" viewBox="0 0 528 745" aria-hidden="true">
    <path d="M0 79 Q264 240 528 79 L528 641 Q264 565 0 641 Z" fill="var(--brand-blue)"/>
  </svg>

  <div class="brand">
    <i class="brand__dot"></i>
    <p class="brand__name">Harlow Ridge Joint &amp; Motion Clinic</p>
  </div>

  <figure class="doctor" style="left:42px;top:175px">
    <span class="doctor__photo" role="img" aria-label="Portrait of Daniel R. Hollis, MD"></span>
    <figcaption><p class="doctor__name">Daniel R. Hollis, MD</p><p class="doctor__role">Orthopedic Surgeon</p></figcaption>
  </figure>
  <figure class="doctor" style="left:156px;top:207px">
    <span class="doctor__photo" role="img" aria-label="Portrait of Gregory T. Amsel, MD"></span>
    <figcaption><p class="doctor__name">Gregory T. Amsel, MD</p><p class="doctor__role">Physical Medicine and Rehabilitation Specialist</p></figcaption>
  </figure>
  <figure class="doctor" style="left:270px;top:171px">
    <span class="doctor__photo" role="img" aria-label="Portrait of Laura J. Pennick, MD MS"></span>
    <figcaption><p class="doctor__name">Laura J. Pennick, MD MS</p><p class="doctor__role">Physical Medicine and Rehabilitation Specialist</p></figcaption>
  </figure>
  <figure class="doctor" style="left:380px;top:216px">
    <span class="doctor__photo" role="img" aria-label="Portrait of R. Evan Morrow, MD"></span>
    <figcaption><p class="doctor__name">R. Evan Morrow, MD</p><p class="doctor__role">Orthopedic Surgeon</p></figcaption>
  </figure>
  <figure class="doctor" style="left:96px;top:388px">
    <span class="doctor__photo" role="img" aria-label="Portrait of Samuel K. Ortner, MD"></span>
    <figcaption><p class="doctor__name">Samuel K. Ortner, MD</p><p class="doctor__role">Orthopedic Surgeon Specializing in spine</p></figcaption>
  </figure>
  <figure class="doctor" style="left:211px;top:416px">
    <span class="doctor__photo" role="img" aria-label="Portrait of Brian L. Keating, Jr., MD"></span>
    <figcaption><p class="doctor__name">Brian L. Keating,Jr., MD</p><p class="doctor__role">Orthopedic Surgeon and Sports Medicine and Shoulder Specialist</p></figcaption>
  </figure>
  <figure class="doctor" style="left:326px;top:394px">
    <span class="doctor__photo" role="img" aria-label="Portrait of Nathan P. Delacroix, MD"></span>
    <figcaption><p class="doctor__name">Nathan P. Delacroix, MD</p><p class="doctor__role">Physical Medicine and Rehabilitation Specialist</p></figcaption>
  </figure>

  <p class="about">Harlow Ridge Joint &amp; Motion Clinic provides leading-edge, results-based care for orthopedic and spine disorders. We are a comprehensive, premier team of specialists dedicated to the diagnosis, treatment, rehabilitation and prevention of sports and orthopedic injuries and conditions. Our team is dedicated to improving the quality of life for our patients and their families.</p>
</section>

<section class="sheet sheet--back">
  <div class="map" role="img" aria-label="Street map showing the practice location"></div>

  <div class="locate">
    <svg width="55" height="97" viewBox="0 0 55 97" aria-hidden="true">
      <path d="M27.5 2 C12 2 2 13 2 27 C2 44 20 62 27.5 88 C35 62 53 44 53 27 C53 13 43 2 27.5 2 Z" fill="var(--pin-red)"/>
      <circle cx="27.5" cy="26" r="10" fill="#5a1410"/>
      <rect x="20" y="88" width="15" height="9" fill="var(--pin-red)"/>
    </svg>
    <span class="locate__label">Locate Here</span>
  </div>

  <address class="contact">
    1450 S. Harlow Road,<br>
    Suite. 120, Fairmont, MO 63199<br>
    <span class="contact__phone">
      <svg width="26" height="26" viewBox="0 0 26 26" aria-hidden="true">
        <circle cx="13" cy="13" r="11.5" fill="none" stroke="var(--ink)" stroke-width="2"/>
        <path d="M9 7.5 l2.4 -0.4 1.2 3 -1.6 1.2 c0.8 1.8 1.8 2.8 3.6 3.6 l1.2 -1.6 3 1.2 -0.4 2.4 c-5 0.6 -9.8 -4.2 -9.4 -9.4z" fill="var(--ink)"/>
      </svg>555-014-2290 1
    </span>
  </address>

  <div class="site-band">
    <svg width="18" height="18" viewBox="0 0 18 18" aria-hidden="true" fill="none" stroke="#fff" stroke-width="1.4">
      <circle cx="9" cy="9" r="7.5"/><ellipse cx="9" cy="9" rx="3.2" ry="7.5"/><path d="M1.5 9h15M3 5h12M3 13h12"/>
    </svg>
    www.harlowridgeclinic.com
  </div>
</section>

</body>
</html>
```